International Conference websites
Halvern Exchange Conference
International Conference websites - Events
Creative Brief
Events
- Conference Info o About the Conference o Conference agenda o workshop Agenda - Keynote o Speakers Directory - Committees o Conference committee directory o Organizing committee directory
Not crowded Please use color in logo as theme color I will upload it.
Elegant
Please check attached logo
top
Mostly we are going to approve design with in 2 or 3 days maximum. Regarding font, You choose one. Topics in this conference which is going to help you in choosing pictures or design Polymers Catalysis Life Sciences & Health Biogenomics & Nanobiology Information Technology Cyber security Machine learning Renewable Energy Renewables/ Renewable storage Water Desalination, waste water reuse Red Sea studies Environment Food security Pollution, crowd management Climate change

```html
<!DOCTYPE html>
<html lang="en">
<head>
<meta charset="utf-8">
<title>Halvern Exchange Conference</title>
<link rel="stylesheet" href="https://fonts.googleapis.com/css2?family=Michroma&family=Open+Sans:wght@400;600;700&family=Oswald:wght@500&family=Montserrat:wght@600;700&display=swap">
<style>
:root{
  --blue:#1f5ea8;
  --navy:#1b2740;
  --teal:#2aa6b5;
  --green:#8cc63f;
  --lime:#d4dd2a;
  --ink:#2b3a55;
  --grey:#8a8f98;
  --line:#e3e6ea;
  --white:#fff;
}
*{box-sizing:border-box;margin:0;padding:0}
html,body{width:1200px;height:4918px;overflow:hidden;background:var(--white)}
body{font-family:"Open Sans",sans-serif;color:var(--ink);position:relative}
.abs{position:absolute}
.heading{font-family:"Michroma",sans-serif;letter-spacing:2px;text-transform:uppercase}
.pill{display:inline-flex;align-items:center;gap:10px;border-radius:30px;font-family:"Michroma",sans-serif;font-size:12px;letter-spacing:1px;text-transform:uppercase}
.pill .dot{width:26px;height:26px;border-radius:50%;border:2px solid #fff;display:inline-block}
.section-title{position:absolute;left:0;width:1200px;text-align:center;font-size:22px;color:var(--blue)}
.title-mark{position:absolute;left:593px;width:14px;height:14px;border-radius:50%;border:2px solid var(--teal)}
.title-rule{position:absolute;left:162px;width:876px;height:1px;background:var(--line)}

/* header */
.site-header{top:0;left:0;width:1200px;height:96px;background:var(--white);display:flex;align-items:center;padding:0 40px}
.brand{display:flex;align-items:center;gap:12px}
.brand-circle{width:46px;height:46px;border-radius:50%;border:4px solid var(--teal)}
.brand-name{font-family:"Open Sans",sans-serif;font-size:12px;font-weight:600;letter-spacing:3px;color:var(--blue);line-height:16px;text-transform:uppercase}
.main-nav{margin-left:auto;display:flex;gap:34px;font-size:12px;font-weight:600;color:#555;text-transform:uppercase}
.main-nav .active{color:var(--blue);border-bottom:2px solid var(--blue);padding-bottom:10px}

/* hero */
.hero{top:96px;left:0;width:1200px;height:600px;background:linear-gradient(180deg,#23405e 0%,#2b7d93 40%,#3fa7b0 70%,#27536f 100%)}
.hero-title{top:462px;left:0;width:1200px;text-align:center;color:#fff;font-size:30px;line-height:38px}
.hero-date{top:542px;left:0;width:1200px;text-align:center;color:#fff;font-size:18px;font-weight:600}
.hero-date::before,.hero-date::after{content:"";display:inline-block;width:120px;height:1px;background:#fff;vertical-align:middle;margin:0 10px}
.hero-register{top:584px;left:525px;width:150px;height:36px;background:var(--green);color:#fff;padding-left:6px}
.hero-arrow{top:340px;width:30px;height:60px}
.countdown{top:668px;left:0;width:1200px;display:flex;justify-content:center;gap:30px}
.count{width:76px;height:76px;border-radius:50%;border:4px solid #fff;color:#fff;display:flex;flex-direction:column;align-items:center;justify-content:center;box-shadow:0 2px 6px rgba(0,0,0,.2)}
.count b{font-family:"Montserrat",sans-serif;font-size:24px;line-height:24px}
.count span{font-size:8px;font-weight:700}
.count.blue{background:var(--blue)}.count.green{background:var(--green)}

/* intro */
.intro-img{top:805px;width:106px;height:170px}
.intro-logo{top:808px;left:548px;display:flex;gap:10px;align-items:center}
.intro-logo .brand-circle{width:42px;height:42px}
.intro-when{top:810px;left:832px;font-family:"Montserrat",sans-serif;font-size:13px;color:var(--ink);letter-spacing:1px;line-height:17px}
.intro-when small{font-size:10px;font-weight:600}
.intro-text{top:880px;left:548px;width:490px;font-size:11px;line-height:22px;color:var(--grey)}
.agenda{top:1030px;width:390px;display:flex;gap:22px}
.agenda-icon{width:90px;height:90px;border-radius:50%;border:3px solid var(--green);display:flex;align-items:center;justify-content:center;flex:none}
.agenda-icon i{width:62px;height:62px;border-radius:50%;background:var(--green);display:block}
.agenda h3{font-family:"Michroma",sans-serif;font-size:12px;color:var(--blue);letter-spacing:1px;margin-top:4px}
.agenda p{font-size:10.5px;line-height:21px;color:var(--grey);margin-top:8px}
.agenda a{font-size:10px;color:var(--blue);display:block;margin-top:8px}
.agenda-divider{top:1030px;left:600px;width:1px;height:110px;background:var(--line)}

/* speakers */
.speakers{top:1215px;left:0;width:1200px;height:708px;background:linear-gradient(180deg,#36a0aa 0%,#2f97a3 60%,#3aa8b0 100%);border-top:4px solid var(--blue)}
.speakers .section-title{top:78px;color:#fff}
.speakers .title-rule{top:117px;background:rgba(255,255,255,.35)}
.speakers .title-mark{top:110px;border-color:#fff}
.speaker{width:150px;height:183px}
.speaker .photo{height:140px;background:linear-gradient(180deg,#c9ccd1,#8f959e)}
.speaker .name{height:43px;background:var(--blue);color:#fff;font-family:"Oswald",sans-serif;font-size:12px;text-transform:uppercase;display:flex;align-items:center;justify-content:center}
.speaker.active .name{background:var(--lime)}
.view-btn{height:34px;border:2px solid #fff;background:var(--green);color:#fff;padding:0 20px 0 4px}

/* topics */
.topics-title{top:1990px}
.tile{display:flex;align-items:flex-end;justify-content:center;padding-bottom:12px;color:#fff;font-family:"Oswald",sans-serif;font-size:13px;text-transform:uppercase}
.t-dark{background:linear-gradient(160deg,#0b1324,#1c3b6a)}
.t-water{background:linear-gradient(180deg,#49b5d3,#0f4f7a)}
.t-space{background:linear-gradient(160deg,#050b1a,#1a4b82)}
.t-ice{background:linear-gradient(180deg,#9fc8e8 0%,#5a8fbf 45%,#1d2f50 100%)}
.t-solar{background:linear-gradient(180deg,#6fa2d0,#2a4d86)}
.t-cyber{background:linear-gradient(180deg,#1f3450,#0a1526)}
.t-chip{background:linear-gradient(160deg,#0f2d59,#1d6fb3)}
.t-net{background:linear-gradient(160deg,#0b1a3a,#2d62b0 60%,#c58a3e)}

/* stats */
.stats{top:2682px;left:0;width:1200px;height:194px;display:flex;border-top:3px solid var(--blue);border-bottom:3px solid var(--blue)}
.stat{flex:1;background:var(--green);display:flex;flex-direction:column;align-items:center;justify-content:center;gap:8px}
.stat.blue{background:var(--blue)}
.stat span{background:#fff;color:var(--teal);font-size:11px;font-weight:700;padding:4px 12px;text-transform:uppercase}
.stat.blue span{color:var(--blue)}
.stat b{font-family:"Montserrat",sans-serif;color:#fff;font-size:32px}

/* companies */
.company{width:154px;height:88px;border:1px solid var(--line);display:flex;align-items:center;justify-content:center;font-size:22px;font-weight:600;color:#9a9ea5}

/* venue */
.venue{top:3453px;left:0;width:1200px;height:472px;background:linear-gradient(180deg,#2c6fb4,#1f5a98 60%,#244c7e)}
.map{top:86px;left:162px;width:417px;height:296px;background:linear-gradient(135deg,#eef0ee,#dfe5e0);border:4px solid #fff}
.venue-logo{top:86px;left:636px;display:flex;gap:20px;align-items:center}
.venue-logo .brand-circle{width:110px;height:110px;border:6px solid #fff}
.venue-logo .brand-name{color:#fff;font-size:18px;letter-spacing:6px;line-height:30px}
.venue-pin{top:238px;left:648px}
.venue-label{top:238px;left:700px;background:#fff;color:var(--blue);font-family:"Michroma",sans-serif;font-size:13px;letter-spacing:2px;padding:3px 18px}
.venue-address{top:270px;left:696px;color:#fff;font-size:17px;font-weight:700;line-height:27px}
.venue-cta{top:345px;left:648px;height:42px;background:#fff;border-radius:30px;display:flex;align-items:center;overflow:hidden}
.venue-cta .when{width:142px;text-align:center;font-size:9px;font-weight:700;color:var(--ink);line-height:11px}
.venue-cta .go{background:var(--green);color:#fff;height:42px;padding:0 34px;display:flex;align-items:center;font-family:"Michroma",sans-serif;font-size:12px;letter-spacing:1px}

/* articles */
.article{top:4087px;width:264px;height:383px;border:1px solid var(--line)}
.article .photo{margin:4px;height:200px;position:relative}
.article .date{position:absolute;left:50%;bottom:0;transform:translateX(-50%);background:var(--teal);color:#fff;font-family:"Michroma",sans-serif;font-size:9px;padding:5px 12px;white-space:nowrap}
.article h4{font-family:"Michroma",sans-serif;font-size:10.5px;text-align:center;line-height:19px;margin:14px 20px 0;color:var(--ink)}
.article p{font-size:10.5px;line-height:22px;color:var(--grey);text-align:center;margin:14px 18px 0}
.article .corner{position:absolute;right:0;bottom:0;width:0;height:0;border-left:40px solid transparent;border-bottom:22px solid #e8eaed}
.article .corner.on{border-bottom-color:var(--teal)}

/* footer */
.site-footer{top:4530px;left:0;width:1200px;height:350px;background:linear-gradient(180deg,#2a3f63,#1b2740 60%,#1a2a48)}
.newsletter{top:120px;left:162px;width:260px;color:#fff}
.newsletter h5{font-family:"Michroma",sans-serif;font-size:18px;letter-spacing:2px;font-weight:400}
.newsletter .bar{width:40px;height:2px;background:#fff;margin:8px 0 10px}
.newsletter p{font-size:10px;line-height:14px}
.newsletter .field{margin-top:10px;height:34px;background:#fff;color:#999;font-size:10px;padding:11px 14px}
.newsletter .subscribe{margin-top:12px;width:148px;height:34px;background:var(--lime);color:var(--navy);font-size:13px;font-weight:700;display:flex;align-items:center;justify-content:center}
.footer-brand{top:112px;left:504px;width:280px}
.footer-brand .brand-name{color:#fff;font-size:18px;letter-spacing:6px;line-height:30px}
.footer-brand p{color:#c9d1de;font-size:10px;line-height:16px;margin-top:14px}
.footer-ring{top:136px;left:890px;width:120px;height:120px;border-radius:50%;border:8px solid #fff}
.socials{top:276px;left:890px;display:flex;gap:10px}
.socials i{width:24px;height:24px;border-radius:50%;border:1.5px solid #fff;display:block}
.bottom-bar{top:4880px;left:0;width:1200px;height:38px;background:var(--blue);color:#fff;font-size:10px;display:flex;align-items:center;padding:0 162px}
.bottom-bar nav{margin-left:auto;display:flex;gap:22px}
</style>
</head>
<body>

<header class="site-header abs">
  <div class="brand"><span class="brand-circle"></span><span class="brand-name">Halvern<br>Exchange<br>Conference</span></div>
  <nav class="main-nav">
    <span class="active">About</span><span>Conference Info</span><span>Keynote</span><span>Committees</span><span>Speakers</span><span>Venue</span><span>Contact</span>
  </nav>
</header>

<section class="hero abs" role="img" aria-label="Aerial photograph of a waterfront city skyline at dusk"></section>
<svg class="abs hero-arrow" style="left:60px" viewBox="0 0 30 60"><path d="M24 4 4 30l20 26" fill="none" stroke="rgba(255,255,255,.6)" stroke-width="2"/></svg>
<svg class="abs hero-arrow" style="left:1110px" viewBox="0 0 30 60"><path d="M6 4l20 26L6 56" fill="none" stroke="rgba(255,255,255,.6)" stroke-width="2"/></svg>
<h1 class="abs heading hero-title">12th International Conference on<br>Life Sciences &amp; Health</h1>
<p class="abs hero-date">12 - 20 March, 2018 / Riyadh, Saudi Arabia</p>
<a class="abs pill hero-register"><span class="dot"></span>Register</a>
<svg class="abs" style="top:630px;left:0" width="1200" height="80" viewBox="0 0 1200 80">
  <path d="M0 30 Q600 90 1200 10 L1200 80 L0 80Z" fill="#fff"/>
  <path d="M0 24 Q600 84 1200 4" fill="none" stroke="#2aa6b5" stroke-width="6"/>
  <path d="M0 36 Q600 96 1200 16" fill="none" stroke="#1f5ea8" stroke-width="3"/>
</svg>
<div class="abs countdown">
  <div class="count blue"><b>25</b><span>DAYS</span></div>
  <div class="count green"><b>08</b><span>HOURS</span></div>
  <div class="count blue"><b>26</b><span>MINUTES</span></div>
  <div class="count green"><b>30</b><span>SECONDS</span></div>
</div>

<div class="abs intro-img" style="left:162px;background:linear-gradient(180deg,#2d5a8a,#163050)" role="img" aria-label="Globe photo, International"></div>
<div class="abs intro-img" style="left:278px;background:linear-gradient(180deg,#8cc63f,#4d8a22)" role="img" aria-label="Green leaf photo, Collaboration"></div>
<div class="abs intro-img" style="left:394px;background:linear-gradient(180deg,#3ab4d8,#1b6e9b)" role="img" aria-label="Blue crowd photo, Conference"></div>
<div class="abs intro-logo"><span class="brand-circle"></span><span class="brand-name" style="font-size:10px;line-height:13px">Halvern<br>Exchange<br>Conference</span></div>
<p class="abs intro-when">JUNE 4–8, 2018,<br><small>RIYADH, SAUDI ARABIA</small></p>
<p class="abs intro-text">Lorem ipsum dolor sit amet, consectetur adipiscing elit. Sed et erat non just vehicula ac non justo. Orci varius natoque penatibus et magnis dis parturient montes ridiculus mus. Sed semper, dui in ultrices faucibus, dolor dui vulputate tellus, et aliquet libero ero eget nullam efficitur sem ut neque vulputate neque fringilla.</p>

<div class="abs agenda" style="left:162px">
  <div class="agenda-icon"><i></i></div>
  <div><h3>Conference Agenda</h3><p>Lorem ipsum dolor sit amet, consec adipiscin elit ed at erat non just vehicul nor penatibus et magnist montes ridiculus.</p><a>READ MORE</a></div>
</div>
<div class="abs agenda-divider"></div>
<div class="abs agenda" style="left:668px">
  <div class="agenda-icon"><i></i></div>
  <div><h3>Workshop Agenda</h3><p>Lorem ipsum dolor sit amet, consec adipiscin elit ed at erat non just vehicul nor penatibus et magnist montes ridiculus.</p><a>READ MORE</a></div>
</div>

<section class="speakers abs" aria-label="Speakers">
  <h2 class="section-title heading">Meet the Speakers</h2>
  <span class="title-rule"></span><span class="title-mark"></span>
  <div class="abs speaker" style="top:149px;left:162px"><div class="photo" role="img" aria-label="Speaker portrait"></div><div class="name">Daniel Brenner</div></div>
  <div class="abs speaker" style="top:149px;left:343px"><div class="photo" role="img" aria-label="Speaker portrait"></div><div class="name">Mei Lin Chao</div></div>
  <div class="abs speaker active" style="top:149px;left:525px"><div class="photo" role="img" aria-label="Speaker portrait"></div><div class="name">Ben Morrow &raquo;</div></div>
  <div class="abs speaker" style="top:149px;left:707px"><div class="photo" role="img" aria-label="Speaker portrait"></div><div class="name">Lara Bentley</div></div>
  <div class="abs speaker" style="top:149px;left:888px"><div class="photo" role="img" aria-label="Speaker portrait"></div><div class="name">Wade Marlow</div></div>
  <div class="abs speaker" style="top:376px;left:162px"><div class="photo" role="img" aria-label="Speaker portrait"></div><div class="name">Colin Sloane</div></div>
  <div class="abs speaker" style="top:376px;left:343px"><div class="photo" role="img" aria-label="Speaker portrait"></div><div class="name">Sheikh Khalid</div></div>
  <div class="abs speaker" style="top:376px;left:525px"><div class="photo" role="img" aria-label="Speaker portrait"></div><div class="name">Erin Garnet</div></div>
  <div class="abs speaker" style="top:376px;left:707px"><div class="photo" role="img" aria-label="Speaker portrait"></div><div class="name">Derek Blane</div></div>
  <div class="abs speaker" style="top:376px;left:888px"><div class="photo" role="img" aria-label="Speaker portrait"></div><div class="name">Nia Ravenna</div></div>
  <a class="abs pill view-btn" style="top:597px;left:486px"><span class="dot"></span>View all Speakers</a>
</section>

<h2 class="section-title heading topics-title">Conference Topics</h2>
<span class="title-rule" style="top:2040px"></span><span class="title-mark" style="top:2033px"></span>
<div class="abs tile t-dark" style="top:2078px;left:162px;width:342px;height:142px" role="img" aria-label="Heartbeat line on a screen">Life Sciences &amp; Health</div>
<div class="abs tile t-water" style="top:2078px;left:518px;width:164px;height:142px" role="img" aria-label="Underwater light">Water</div>
<div class="abs tile t-space" style="top:2078px;left:695px;width:342px;height:142px" role="img" aria-label="Glowing cells">Biogenomics &amp; Nanobiology</div>
<div class="abs tile t-ice" style="top:2235px;left:162px;width:163px;height:295px" role="img" aria-label="Iceberg above and below water">Climate Change</div>
<div class="abs tile t-solar" style="top:2235px;left:338px;width:344px;height:139px" role="img" aria-label="Solar panels and wind turbines">Renewables/ Renewable Storage</div>
<div class="abs tile t-cyber" style="top:2388px;left:338px;width:166px;height:142px" role="img" aria-label="Hooded figure at a computer">Cyber Security</div>
<div class="abs tile t-chip" style="top:2388px;left:518px;width:164px;height:142px" role="img" aria-label="Glowing processor chip">Machine Learning</div>
<div class="abs tile t-net" style="top:2235px;left:695px;width:342px;height:295px" role="img" aria-label="Hand touching a digital network over a city">Information Technology</div>
<a class="abs pill view-btn" style="top:2566px;left:498px;border-color:var(--green)"><span class="dot"></span>View all Topics</a>

<section class="stats abs" aria-label="Statistics">
  <div class="stat"><span>Attendees</span><b>25,000</b></div>
  <div class="stat blue"><span>CEOs</span><b>3,750+</b></div>
  <div class="stat"><span>Companies</span><b>5,600+</b></div>
  <div class="stat"><span>Countries</span><b>120+</b></div>
</section>

<h2 class="section-title heading" style="top:2952px">Participated Companies</h2>
<span class="title-rule" style="top:2994px"></span><span class="title-mark" style="top:2987px"></span>
<div class="abs company" style="top:3043px;left:162px">Graviton</div>
<div class="abs company" style="top:3043px;left:343px">Corvale</div>
<div class="abs company" style="top:3043px;left:525px">Palisade</div>
<div class="abs company" style="top:3043px;left:707px">Tamra</div>
<div class="abs company" style="top:3043px;left:888px">Coinlane</div>
<div class="abs company" style="top:3161px;left:162px">Workora</div>
<div class="abs company" style="top:3161px;left:343px">Quarzel</div>
<div class="abs company" style="top:3161px;left:525px">Linkvale</div>
<div class="abs company" style="top:3161px;left:707px">Roomly</div>
<div class="abs company" style="top:3161px;left:888px">Tileforge</div>
<div class="abs company" style="top:3281px;left:162px">Starfield</div>
<div class="abs company" style="top:3281px;left:343px">Riverstone</div>
<div class="abs company" style="top:3281px;left:525px">Netmesh</div>
<div class="abs company" style="top:3281px;left:707px">Halcyon</div>
<div class="abs company" style="top:3281px;left:888px">Ascendo</div>

<section class="venue abs" aria-label="Venue">
  <div class="abs map" role="img" aria-label="Street map of the venue area in Riyadh with a marker"></div>
  <div class="abs venue-logo"><span class="brand-circle"></span><span class="brand-name">Halvern<br>Exchange<br>Conference</span></div>
  <svg class="abs venue-pin" width="30" height="36" viewBox="0 0 30 36"><path d="M15 2a10 10 0 0 0-10 10c0 8 10 18 10 18s10-10 10-18A10 10 0 0 0 15 2z" fill="none" stroke="#fff" stroke-width="2"/><circle cx="15" cy="12" r="3.5" fill="none" stroke="#fff" stroke-width="2"/><path d="M4 34h22" stroke="#fff" stroke-width="2"/></svg>
  <span class="abs venue-label">Venue</span>
  <p class="abs venue-address">4120, Palm Crescent Road Tower 2, ALNOOR,<br>RIYADH 11860, Saudi Arabia</p>
  <div class="abs venue-cta"><span class="when">JUNE 4–8, 2018<br>RIYADH, SA</span><span class="go">Register Now</span></div>
</section>

<h2 class="section-title heading" style="top:3995px">Latest Articles</h2>
<span class="title-rule" style="top:4037px"></span><span class="title-mark" style="top:4030px"></span>
<article class="abs article" style="left:166px">
  <div class="photo" style="background:linear-gradient(180deg,#3a1a14,#a8452a)" role="img" aria-label="Speaker on stage before an audience"><span class="date">12 March, 2018</span></div>
  <h4>Lorem ipsu conse ctetur adipiscing proin fel</h4>
  <p>adipiscing elit ullam dignissim ligula Lorem ipsum dolor sit amet, consectetur at congue ullamcorper lorem.</p>
  <span class="corner"></span>
</article>
<article class="abs article" style="left:468px">
  <div class="photo" style="background:linear-gradient(180deg,#e3b372,#6d6a4a)" role="img" aria-label="Wind turbines on hills at sunset"><span class="date">10 March, 2018</span></div>
  <h4>Lorem ipsu conse ctetur adipiscing proin fel</h4>
  <p>adipiscing elit ullam dignissim ligula Lorem ipsum dolor sit amet, consectetur at congue ullamcorper lorem.</p>
  <span class="corner on"></span>
</article>
<article class="abs article" style="left:772px">
  <div class="photo" style="background:linear-gradient(180deg,#eaf3fb,#5ea4d8)" role="img" aria-label="Cloud computing concept above a tablet"><span class="date">08 March, 2018</span></div>
  <h4>Lorem ipsu conse ctetur adipiscing proin fel</h4>
  <p>adipiscing elit ullam dignissim ligula Lorem ipsum dolor sit amet, consectetur at congue ullamcorper lorem.</p>
  <span class="corner"></span>
</article>

<footer class="site-footer abs" role="contentinfo">
  <div class="abs newsletter">
    <h5>Newsletter</h5><div class="bar"></div>
    <p>Never miss another speaker announcement. Join over 1 million newsletter subscribers.</p>
    <div class="field">Enter Email</div>
    <div class="subscribe">SUBSCRIBE</div>
  </div>
  <div class="abs footer-brand">
    <span class="brand-name">Halvern<br>Exchange<br>Conference</span>
    <p>Lorem ipsum dolor sit amet, conse adipiscing elit. Donec et dignissim ante, quis cur enean suscipit massa non ex sodales, vitae volutpat ligula vehicul donec sed semper nunc.</p>
  </div>
  <span class="abs footer-ring"></span>
  <div class="abs socials" aria-label="Social links"><i></i><i></i><i></i><i></i></div>
</footer>
<svg class="abs" style="top:4500px;left:0" width="1200" height="70" viewBox="0 0 1200 70">
  <path d="M0 0 L1200 0 L1200 20 Q600 70 0 30Z" fill="#fff"/>
  <path d="M0 30 Q600 70 1200 20" fill="none" stroke="#2aa6b5" stroke-width="6"/>
  <path d="M0 40 Q600 80 1200 30" fill="none" stroke="#1f5ea8" stroke-width="3"/>
</svg>
<div class="abs bottom-bar">
  <span>© COPYRIGHT 2018 HALVERN EXCHANGE CONFERENCE.</span>
  <nav><span>CONTACT</span><span>PRIVACY</span><span>SITEMAP</span></nav>
</div>

</body>
</html>
```